Essential oil label for bottles

Looking to modify our current logo and label design. It looks too simple. I will attach images of our competitors to use as examples. Our company name is Lunvessa. We have 2 different bottles. Clear and amber color. Going forward, we will be using only the amber bottle. The other 2 images are the biggest sellers brands. We want to make some adjustments to ours.

Target Market(s)

Tradeport sales

Industry/Entity Type

Essential oil, perfume

Colors

Designer to choose only greyscale colors for use in the design.

Requirements
Nice to have
• A slight change to fonts and logo design. Maybe change the font and design of the word "Lunvessa" in our logo. Maybe add something to the label to make it stand out more but still keeping it clean and modern
Should not have
• No colors, besides, black, grays, whites, and off white.

```html
<!DOCTYPE html>
<html lang="en">
<head>
<meta charset="UTF-8">
<title>Lunvessa – Sea Veil Fragrance Oil Label</title>
<link rel="stylesheet" href="https://fonts.googleapis.com/css2?family=Comfortaa:wght@500&family=Heebo:wght@400&family=Montserrat:wght@400;500&display=swap">
<style>
  :root {
    --backdrop: #d9d8d3;
    --label-white: #ffffff;
    --band-black: #221f20;
    --cream: #f5efdc;
    --ink: #1c1a1b;
  }
  * { margin: 0; padding: 0; box-sizing: border-box; }
  html, body {
    width: 1200px;
    height: 900px;
    overflow: hidden;
    background: var(--backdrop);
  }
  .canvas {
    position: relative;
    width: 1200px;
    height: 900px;
  }
  .label {
    position: absolute;
    left: 333px;
    top: 50px;
    width: 533px;
    height: 800px;
    background: var(--label-white);
    box-shadow: 0 6px 24px rgba(0,0,0,0.08);
  }
  .brand {
    position: absolute;
    top: 92px;
    left: 0;
    width: 100%;
    text-align: center;
  }
  .brand-dot {
    display: block;
    width: 18px;
    height: 18px;
    margin: 0 auto 16px;
    border-radius: 50%;
    background: var(--ink);
  }
  .brand-name {
    font-family: "Montserrat", sans-serif;
    font-weight: 400;
    font-size: 40px;
    letter-spacing: 1px;
    color: var(--ink);
    line-height: 1;
  }
  .band {
    position: absolute;
    top: 256px;
    left: 0;
    width: 533px;
    height: 330px;
  }
  .band-shape { fill: var(--band-black); }
  .product-name {
    position: absolute;
    top: 408px;
    left: 0;
    width: 100%;
    text-align: center;
    font-family: "Comfortaa", sans-serif;
    font-weight: 500;
    font-size: 72px;
    line-height: 1;
    color: var(--cream);
    letter-spacing: 3px;
    transform: translateY(-50%);
  }
  .product-type {
    position: absolute;
    top: 494px;
    left: 0;
    width: 100%;
    text-align: center;
    font-family: "Montserrat", sans-serif;
    font-weight: 500;
    font-size: 23px;
    line-height: 1;
    letter-spacing: 6px;
    color: var(--cream);
    padding-left: 6px;
  }
  .product-rule {
    position: absolute;
    top: 541px;
    left: 101px;
    width: 335px;
    height: 2px;
    background: var(--cream);
  }
  .notes {
    position: absolute;
    top: 663px;
    left: 0;
    width: 100%;
    text-align: center;
    font-family: "Heebo", sans-serif;
    font-weight: 400;
    font-size: 27px;
    color: var(--ink);
    line-height: 44px;
  }
  .notes .divider { padding: 0 6px; }
</style>
</head>
<body>
<main class="canvas">
  <section class="label">
    <header class="brand">
      <span class="brand-dot"></span>
      <div class="brand-name">LUNVESSA</div>
    </header>

    <svg class="band" viewBox="0 0 533 330" aria-hidden="true">
      <path class="band-shape" d="M0 16 Q14.8 0 29.6 16 T59.2 16 T88.8 16 T118.4 16 T148 16 T177.6 16 T207.2 16 T236.8 16 T266.4 16 T296 16 T325.6 16 T355.2 16 T384.8 16 T414.4 16 T444 16 T473.6 16 T503.2 16 T532.8 16 L533 16 L533 314 L532.8 314 Q518 330 503.2 314 T473.6 314 T444 314 T414.4 314 T384.8 314 T355.2 314 T325.6 314 T296 314 T266.4 314 T236.8 314 T207.2 314 T177.6 314 T148 314 T118.4 314 T88.8 314 T59.2 314 T29.6 314 T0 314 Z"/>
    </svg>

    <h1 class="product-name">Sea Veil</h1>
    <p class="product-type">FRAGRANCE OIL</p>
    <div class="product-rule"></div>

    <div class="notes">
      <p>WHITE TEA<span class="divider">|</span>ORANGE<span class="divider">|</span>PALO SANTO</p>
      <p>200 ML</p>
    </div>
  </section>
</main>
</body>
</html>
```